Top Google Reviewed Exterior Cleaning Company Needs A Fresh New Brand & Logo Design

I need a new logo / brand design to wrap my large "Roadmule" cargo vans. I am looking for something fresh and not too busy that will turn heads whenever our trucks are seen. I want to change the name to "Bright Harbor Home Wash Crew" with a tag line that say's " Your Neighborhood's Trusted Choice " I love the colors and layout in the attached picture of "Dunmore Plumbing & Heating. In case you can't open that picture that company website is dunmoremechworks.example the van is on this website. Please check out my website harborwashLi.example to see my current wraps. I definitely want to get away from the bubbles I currently have on the wraps. I have also uploaded my current logo. I would like to incorporate the house and tree of my current logo but give it a fresh look if possible although I am open to all ideas. The current company name is "Bright Harbor Cleaning Services"Thank You

```html
<!DOCTYPE html>
<html lang="en">
<head>
<meta charset="utf-8">
<title>Bright Harbor Home Wash Crew – Van Wrap</title>
<link href="https://fonts.googleapis.com/css2?family=Poppins:wght@400;600;700;800&display=swap" rel="stylesheet">
<style>
  :root{
    --wrap-orange:#e8681e;
    --wrap-navy:#1c1f5e;
    --wrap-white:#f1f1f1;
    --trim-black:#242424;
    --glass:#2e2e30;
    --tyre:#1a1a1a;
    --rim:#9a9a9a;
    --lamp:#d8d8d8;
    --tail-red:#b3262c;
    --page:#ffffff;
  }
  html,body{margin:0;padding:0;width:1200px;height:1200px;overflow:hidden;background:var(--page);}
  .canvas{display:block;width:1200px;height:1200px;}
  text{font-family:"Poppins",sans-serif;}
  .brand-name{font-weight:800;fill:var(--wrap-navy);letter-spacing:.4px;}
  .brand-name.on-orange{fill:#fff;}
  .tagline{font-weight:400;fill:var(--wrap-navy);}
  .tagline.on-orange{fill:#fff;}
  .service{font-weight:600;fill:#fff;}
  .phone{font-weight:700;fill:#fff;}
  .web{font-weight:600;fill:#fff;}
</style>
</head>
<body>
<svg class="canvas" viewBox="0 0 1200 1200" xmlns="http://www.w3.org/2000/svg" role="img" aria-label="Bright Harbor van wrap shown on side, front and rear views">
  <defs>
    <clipPath id="side-body">
      <path d="M150 420 L156 368 Q163 336 212 324 L300 300 L392 214 Q430 150 560 142 L1010 138 Q1030 140 1034 165 L1046 300 L1048 440 L150 440 Z"/>
    </clipPath>
    <clipPath id="rear-body">
      <path d="M690 700 Q700 640 760 632 L1010 632 Q1070 640 1078 700 L1082 1000 L686 1000 Z"/>
    </clipPath>
  </defs>

  <!-- SIDE VIEW -->
  <g class="van-side">
    <g clip-path="url(#side-body)">
      <rect class="side-white" x="140" y="130" width="920" height="320" fill="var(--wrap-white)"/>
      <polygon class="side-orange" points="140,130 716,130 525,395 140,395" fill="var(--wrap-orange)"/>
      <polygon class="side-navy-band" points="560,345 1060,300 1060,400 525,400" fill="var(--wrap-navy)"/>
      <rect class="side-stripe" x="140" y="393" width="920" height="5" fill="var(--wrap-white)"/>
      <rect class="side-rocker" x="140" y="398" width="920" height="50" fill="var(--trim-black)"/>
      <rect class="side-rocker-stripe" x="370" y="436" width="440" height="10" fill="var(--wrap-navy)"/>
    </g>
    <polygon class="side-window" points="335,292 395,222 475,215 468,315 340,335" fill="var(--glass)"/>
    <rect class="front-bumper" x="146" y="405" width="60" height="50" rx="10" fill="var(--trim-black)"/>
    <rect class="rear-bumper" x="990" y="405" width="60" height="50" rx="8" fill="var(--trim-black)"/>
    <circle cx="295" cy="470" r="56" fill="var(--tyre)"/>
    <circle cx="295" cy="470" r="30" fill="var(--rim)"/>
    <circle cx="878" cy="470" r="56" fill="var(--tyre)"/>
    <circle cx="878" cy="470" r="30" fill="var(--rim)"/>

    <g class="service-list">
      <text class="service" x="502" y="209" font-size="10">| Gentle Roof Soft Washing</text>
      <text class="service" x="502" y="238" font-size="10">| Pressure Washing</text>
      <text class="service" x="502" y="266" font-size="10">| Window Cleaning</text>
      <text class="service" x="502" y="294" font-size="10">| Gutter Cleaning</text>
    </g>
    <g class="brand-lockup">
      <rect x="728" y="216" width="14" height="14" fill="var(--wrap-navy)"/>
      <text class="brand-name" x="752" y="236" font-size="19">BRIGHT HARBOR</text>
      <text class="brand-name" x="752" y="259" font-size="19">HOME WASH CREW</text>
      <text class="tagline" x="752" y="274" font-size="8">Your Neighborhood's Trusted Choice</text>
    </g>
    <text class="phone" x="996" y="340" font-size="19" text-anchor="end">555-555-0142</text>
    <text class="web" x="996" y="354" font-size="8.5" text-anchor="end">www.BrightHarborWash.example</text>
  </g>

  <!-- FRONT VIEW -->
  <g class="van-front">
    <path d="M150 700 Q160 625 260 620 L460 620 Q540 625 548 700 L555 900 L140 900 Z" fill="var(--wrap-orange)"/>
    <rect x="70" y="785" width="45" height="75" rx="10" fill="var(--trim-black)"/>
    <rect x="582" y="790" width="45" height="75" rx="10" fill="var(--trim-black)"/>
    <path d="M160 700 Q165 690 180 690 L480 690 Q495 690 500 705 L490 830 L170 830 Z" fill="var(--glass)"/>
    <ellipse cx="165" cy="900" rx="38" ry="30" fill="var(--lamp)"/>
    <ellipse cx="495" cy="900" rx="38" ry="30" fill="var(--lamp)"/>
    <path d="M97 960 L100 1100 Q105 1125 140 1125 L540 1125 Q575 1125 578 1100 L580 960 L540 980 L140 980 Z" fill="var(--trim-black)"/>
    <rect x="195" y="905" width="250" height="95" rx="18" fill="#3a3a3a"/>
    <rect x="105" y="1095" width="60" height="50" rx="8" fill="var(--tyre)"/>
    <rect x="515" y="1095" width="60" height="50" rx="8" fill="var(--tyre)"/>
    <g class="brand-lockup">
      <rect x="240" y="862" width="8" height="8" fill="#fff"/>
      <text class="brand-name on-orange" x="254" y="872" font-size="10">BRIGHT HARBOR</text>
      <text class="brand-name on-orange" x="254" y="884" font-size="10">HOME WASH CREW</text>
      <text class="tagline on-orange" x="254" y="892" font-size="4.5">Your Neighborhood's Trusted Choice</text>
    </g>
  </g>

  <!-- REAR VIEW -->
  <g class="van-rear">
    <g clip-path="url(#rear-body)">
      <rect x="680" y="620" width="410" height="390" fill="var(--wrap-white)"/>
      <rect class="rear-navy-band" x="680" y="848" width="410" height="135" fill="var(--wrap-navy)"/>
    </g>
    <rect x="810" y="625" width="140" height="16" rx="8" fill="var(--trim-black)"/>
    <line x1="880" y1="645" x2="880" y2="985" stroke="#bdbdbd" stroke-width="1.5"/>
    <rect x="676" y="848" width="22" height="110" rx="6" fill="var(--tail-red)"/>
    <rect x="1070" y="848" width="22" height="110" rx="6" fill="var(--tail-red)"/>
    <path d="M672 985 L1094 985 L1090 1080 Q1085 1100 1060 1100 L705 1100 Q680 1100 676 1080 Z" fill="var(--trim-black)"/>
    <rect x="690" y="1100" width="55" height="55" rx="8" fill="var(--tyre)"/>
    <rect x="1020" y="1100" width="55" height="55" rx="8" fill="var(--tyre)"/>
    <g class="brand-lockup">
      <rect x="772" y="732" width="14" height="14" fill="var(--wrap-navy)"/>
      <text class="brand-name" x="796" y="752" font-size="19">BRIGHT HARBOR</text>
      <text class="brand-name" x="796" y="775" font-size="19">HOME WASH CREW</text>
      <text class="tagline" x="796" y="790" font-size="8">Your Neighborhood's Trusted Choice</text>
    </g>
    <g class="service-list">
      <text class="service" x="730" y="875" font-size="8.5">| Gentle Roof Soft Washing</text>
      <text class="service" x="730" y="891" font-size="8.5">| Pressure Washing</text>
      <text class="service" x="730" y="907" font-size="8.5">| Window Cleaning</text>
      <text class="service" x="730" y="923" font-size="8.5">| Gutter Cleaning</text>
    </g>
    <text class="phone" x="730" y="960" font-size="16">555-555-0142</text>
    <text class="web" x="730" y="972" font-size="7">www.BrightHarborWash.example</text>
  </g>
</svg>
</body>
</html>
```